Business card for Eyelash extension salon in Beverly Hills,California USA

We need new business card for our salon in Beverly Hills. The salon name is 'Lumarra' . We would like to have...Business name: Lumarra Name of person: will provide later Address 6128 N.Corbel Ridge Blvd Beverly Hills , CA 90210 Phone: will provide later (Text only) Web: www.lumarrastudio-example.com Pictogrid icon, Friendvale icon follow us for seasonal campaign and news @lumarrastudioexample Design should look elegant, high-end, clean, simple, cohesive with my brand. Please refer my brand board. Business name color will be metallic bronzy color. Im thinking grey background or white background. Thanks

Target Market(s)

25-35. Gender neutral. People who are in Entertainment business industry.
This is High-end Eyelash extension salon in Beverly Hills

Industry/Entity Type

Beauty Salon

Contact Information for Business Card

Business name: Lumarra
Name of person: will provide later
Address 6128 N.Corbel Ridge Blvd Beverly Hills , CA 90210
Phone: will provide later (Text only)
Web: www.lumarrastudio-example.com
Pictogrid icon, Friendvale icon
follow us for seasonal campaign and news @lumarrastudioexample

Requirements
Must have
• Beautiful, elegant, clean and simple look but very attractive and modern
Should not have
• We don't like too clutter, too busy designs.

```html
<!DOCTYPE html>
<html lang="en">
<head>
<meta charset="utf-8">
<title>Lumarra Business Card</title>
<link rel="stylesheet" href="https://fonts.googleapis.com/css2?family=Playfair+Display:wght@400;700&display=swap">
<style>
  :root {
    --backdrop: #e6e4e1;
    --card: #353535;
    --bronze: #a57a52;
    --ink-light: #f2efea;
  }
  * { box-sizing: border-box; margin: 0; padding: 0; }
  html, body { width: 1200px; height: 912px; overflow: hidden; background: var(--backdrop); }
  .canvas {
    width: 1200px; height: 912px;
    display: flex; align-items: center; justify-content: center; gap: 40px;
    font-family: "Playfair Display", Georgia, serif;
  }
  .card {
    width: 540px; height: 309px;
    background: var(--card);
    border-radius: 22px;
    position: relative;
    color: var(--ink-light);
    text-align: center;
  }
  /* Front */
  .brand-name {
    position: absolute; left: 0; right: 0; top: 88px;
    font-size: 60px; font-weight: 400; color: var(--bronze);
    letter-spacing: 1px; line-height: 1;
  }
  .social-row {
    position: absolute; left: 0; right: 0; top: 192px;
    display: flex; justify-content: center; gap: 18px;
    font-size: 11px; letter-spacing: 0.5px;
  }
  .social-row span { display: inline-flex; align-items: center; gap: 6px; }
  .social-row span::before {
    content: ""; width: 10px; height: 10px; background: var(--ink-light); border-radius: 2px;
  }
  .follow-line {
    position: absolute; left: 0; right: 0; top: 222px;
    font-size: 14px;
  }
  /* Back */
  .person-name {
    position: absolute; left: 0; right: 0; top: 62px;
    font-size: 23px; font-weight: 700; color: var(--bronze); letter-spacing: 1px;
  }
  .person-role { position: absolute; left: 0; right: 0; top: 94px; font-size: 13px; }
  .contact-list {
    position: absolute; left: 0; right: 0; top: 128px;
    list-style: none; font-size: 14px; line-height: 25px;
  }
  .contact-list .phone { margin-bottom: 8px; }
  .address {
    position: absolute; left: 0; right: 0; bottom: 36px;
    font-size: 13.5px; color: var(--bronze);
  }
</style>
</head>
<body>
<main class="canvas">
  <section class="card card-front">
    <h1 class="brand-name">Lumarra</h1>
    <div class="social-row">
      <span>Friendvale</span>
      <span>Pictogrid</span>
    </div>
    <p class="follow-line">Follow us for seasonal campaign and news @lumarrastudioexample</p>
  </section>

  <section class="card card-back">
    <h2 class="person-name">MIRA CASTELL</h2>
    <p class="person-role">Manager</p>
    <ul class="contact-list">
      <li class="phone">310-555-0147</li>
      <li>info@lumarrastudio-example.com</li>
      <li>www.lumarrastudio-example.com</li>
    </ul>
    <p class="address">6128 N.Corbel Ridge Blvd Beverly Hills, CA 90210</p>
  </section>
</main>
</body>
</html>
```